バックとタイトルにひと工夫があるとうれしいです。コピー等は入れてもらってかまいません。
添付するイラレデータCS2に全ての内容をいれます。ただし上部の大きな写真2点は本日撮り直しますので明日にでも追加でアップします。
• 高解像度JPG (.jpg)
• イラストレーター形式 (.ai)
原稿内容が一部変更になり、撮影した写真を入れておきます。はじめに添付したファイルと差し替えてください。
貼ってある写真は解像度を落としてありますので決定時に高解像度と入れ替えていただきます。
すみません。原稿1点追加になりました。

4,200円以上の宴会料理&15名様以上でいも又は麦焼酎(4合)をサービス!!
※期間 平成24年1月末日まで ※月・水・木曜日のみ

上記2行と焼酎の写真を入れてください。よろしく御願いします。

とても賑やかで、なお和のイメージが良く出ていてとても気に入りました。文字が読みづらいところが少々ありましたが訂正して頂くより自分で直した方が早いと手を加えさせていただきました。全体的なイメージはとても良かったです。

良いデザインを作成していただきありがとうございます。また依頼することがありますのでよろしくお願いします。

```html
<!DOCTYPE html>
<html lang="ja">
<head>
<meta charset="utf-8">
<title>忘・新年会 ご宴会プラン</title>
<link href="https://fonts.googleapis.com/css2?family=Shippori+Mincho+B1:wght@500;700;800&family=Noto+Sans+JP:wght@400;700&display=swap" rel="stylesheet">
<style>
:root{
  --ink:#0b0a08;
  --gold:#d9b45a;
  --gold-light:#f4df9c;
  --red:#b3121b;
  --deep-red:#7a0d12;
  --paper:#f6f1e6;
  --white:#ffffff;
  --text-dark:#2a1a12;
}
*{box-sizing:border-box;margin:0;padding:0}
html,body{width:872px;height:1200px;overflow:hidden}
body{
  background:radial-gradient(ellipse at 30% 20%,#2a2318 0%,var(--ink) 60%);
  font-family:"Noto Sans JP",sans-serif;color:var(--white);position:relative;
}
.abs{position:absolute}
.mincho{font-family:"Shippori Mincho B1",serif}
.photo{position:absolute;border-radius:4px}
.photo--food{background:radial-gradient(circle at 40% 50%,#8a6a3e,#3d2a18 70%,#1a120b)}
.photo--warm{background:radial-gradient(circle at 50% 50%,#c2884a,#5a3218 75%)}
.photo--pot{background:radial-gradient(circle at 50% 55%,#b7643a,#3a1d10 80%)}

.title{left:22px;top:10px;font-weight:800;font-size:58px;line-height:1.12;letter-spacing:2px;
  background:linear-gradient(180deg,var(--gold-light),var(--gold) 55%,#9b7a2e);
  -webkit-background-clip:text;background-clip:text;color:transparent}
.lead{left:470px;top:12px;width:390px;font-size:13px;line-height:1.6;color:var(--white)}
.tag{display:inline-block;background:var(--red);color:var(--white);font-weight:700;font-size:17px;padding:3px 10px;font-family:"Shippori Mincho B1",serif}
.note{font-size:11px;color:var(--white)}
.pricebox{background:var(--white);color:var(--text-dark);padding:4px 12px;text-align:right;font-weight:700}
.price{color:var(--red);font-family:"Shippori Mincho B1",serif;font-weight:800}

.plan{left:470px;width:390px}
.plan-row{display:flex;align-items:center;justify-content:space-between;margin-bottom:4px}

.promo{left:450px;top:295px;width:410px;height:90px;border:2px solid var(--gold);background:linear-gradient(90deg,var(--deep-red),#3a0608);padding:10px 110px 10px 14px;font-size:14px;line-height:1.5;font-weight:700}
.promo small{display:block;font-size:10px;font-weight:400;color:var(--gold-light);margin-top:4px}
.promo .photo{right:8px;top:6px;width:90px;height:74px;background:linear-gradient(180deg,#3b2a1a,#0e0a06)}

.event{left:15px;top:348px;width:425px;height:180px;background:var(--paper);color:var(--deep-red);text-align:center;padding-top:16px;border:3px solid var(--gold)}
.event .sub{font-size:22px;font-weight:700}
.event .main{font-size:52px;font-weight:800;line-height:1.15;color:var(--red)}
.event .dates{font-size:24px;font-weight:800;color:var(--text-dark)}
.event .limit{font-size:14px;color:var(--text-dark)}

.section{left:15px;width:425px}
.aya-price{font-size:15px;margin-top:8px}
.aya-price .price{font-size:38px;color:var(--gold-light)}
.list{list-style:none;font-size:14px;line-height:1.75;margin-top:6px}
.list li{display:flex;justify-content:space-between;width:200px;border-bottom:1px dotted #6b5a3a}

.osechi{left:15px;top:880px;width:425px;height:300px;border:1px solid var(--gold);padding:12px}
.nabe{left:450px;top:720px;width:410px}
.nabe-head{background:var(--white);color:var(--red);font-size:19px;font-weight:800;text-align:center;padding:8px;font-family:"Shippori Mincho B1",serif}
</style>
</head>
<body>
<h1 class="abs title mincho">忘・新年会<br>ご宴会プラン</h1>
<p class="abs lead mincho">ひときわ宴を盛り上げてくれる<br>美味しいお料理をご用意いたしました。</p>

<div class="abs plan" style="top:70px">
  <div class="plan-row"><span class="tag">宴会料理</span><span class="note">要予約(2名様より)</span></div>
  <div class="pricebox"><span class="price" style="font-size:26px">3,675</span>円(税込)より</div>
</div>
<div class="abs plan" style="top:152px">
  <div class="plan-row"><span class="tag">飲み放題</span><span class="note">要予約(2名様より)</span></div>
  <div class="pricebox">宴会料理+<span class="price" style="font-size:24px">1,575</span>円</div>
  <p class="note" style="margin-top:6px">一人飲み放題のみのご利用もできます。</p>
  <div class="pricebox" style="margin-top:4px;margin-left:180px"><span class="price" style="font-size:22px">1,200</span>円(税込)</div>
</div>

<div class="photo photo--food" style="left:15px;top:150px;width:440px;height:185px" role="img" aria-label="宴会料理の写真"></div>

<div class="abs promo">4,200円以上の宴会料理&amp;15名様以上で<br>いも又は麦焼酎(4合)をサービス!!
  <small>※期間 平成24年1月末日まで ※月・水・木曜日のみ</small>
  <div class="photo" role="img" aria-label="焼酎の写真"></div>
</div>

<div class="abs event mincho">
  <div class="sub">日頃のご来店に感謝して</div>
  <div class="main">冬の特別企画</div>
  <div class="dates">11月1日(木)〜16日(金)</div>
  <div class="limit">平日昼限定(土・日・祝日除く)</div>
</div>

<div class="photo photo--warm" style="left:450px;top:395px;width:410px;height:150px" role="img" aria-label="お昼膳の写真"></div>
<div class="photo photo--food" style="left:450px;top:555px;width:410px;height:150px" role="img" aria-label="料理の写真"></div>

<div class="abs section" style="top:545px">
  <span class="tag">レディースお昼膳「綾」</span>
  <p class="aya-price mincho">通常2,100円を <span class="price">1,575</span>円(税込)</p>
  <p class="note">※ご予約の方優先となります。数に限りがございます。</p>
</div>

<div class="abs section" style="top:670px">
  <span class="tag">冬のレディースお昼膳</span>
  <ul class="list mincho">
    <li><span>雅 膳</span><span>1,575円</span></li>
    <li><span>彩 膳</span><span>2,100円</span></li>
    <li><span>華 膳</span><span>2,625円</span></li>
    <li><span>極 膳</span><span>3,150円</span></li>
  </ul>
</div>
<div class="photo photo--warm" style="left:235px;top:675px;width:205px;height:180px" role="img" aria-label="レディースお昼膳の写真"></div>

<div class="abs osechi">
  <span class="tag">おせち料理</span> <span class="note">要予約</span>
  <ul class="list mincho">
    <li><span>二段重</span><span>21,000円</span></li>
    <li><span>一段重</span><span>15,750円</span></li>
  </ul>
  <p class="note" style="margin-top:10px;width:200px;line-height:1.6">※12月25日までにご予約ください。31日お渡しとなります。</p>
  <div class="photo photo--food" style="right:12px;top:12px;width:190px;height:274px" role="img" aria-label="おせち料理の写真"></div>
</div>

<div class="abs nabe">
  <div class="nabe-head">鍋コースは全て刺身付きとなります</div>
  <p class="mincho" style="margin-top:8px;font-size:15px;color:var(--gold-light)">2名様よりお受け致します</p>
  <ul class="list mincho" style="width:200px">
    <li><span>ふぐコース</span><span></span></li>
    <li><span>すっぽんコース</span><span></span></li>
    <li><span>かにコース</span><span></span></li>
  </ul>
  <div class="pricebox" style="margin-top:10px;width:200px"><span class="price" style="font-size:24px">5,250</span>円(税込)より</div>
  <p class="note" style="margin-top:12px;width:200px">一人鍋もございます</p>
  <div class="pricebox" style="margin-top:6px;width:200px"><span class="price" style="font-size:22px">1,200</span>円(税込)より</div>
  <div class="photo photo--pot" style="left:215px;top:100px;width:195px;height:355px" role="img" aria-label="鍋料理の写真"></div>
</div>
</body>
</html>
```